INFOGRAPHIC DESING GYM SCHEDULE . FULL SCHEDULE AND CLASSES ROON SCHEDULE

I NEED TO CREATED A DESIGN FOR COMPLETE SCHEDULE TAMPLE FOR OUR GYM
AND SMALL SCHEDULE FOR EACH ROON OF THE GYM AND THE CLASSES THTA HAPPEN IN THE ROON
THE SCHEDULE WILL HAVE
CLASSES SCHEDULE
CLASSE DESCRIPTION
AND GRAPHIC EXPLAN HOW EFFECTIVE THE CLASSES ARE IN SOME IMPORT FECTOR .
I MAKE MY SELF A SAMPLE AND WILL UP LOAD IT NO WEEL DONE, BUT YOU CAN HAVE AN IDEIA
II LIKE TO MAKE IT BETTER AND MORE PROFESSIONAL .
RIGHT NOW WE CAN HAVE ALL AS PLACE HOLDER
Updates

hello i never got any other file right now i am very frustrated with this servese i spend a lot of monet for a design this experience is far from been good

Target Market(s)

gym

Font styles to use
Sans Serif

Colors
ec1f27
000000
9d9d9d

Requirements
Must have
• MUST HAVE A UNIQUE DESIGN . WILL USE ALL OF OUR GYM AND WILL NEED TO HAVE A PERSOLIZED DESIGN .
• WE NEED TO HAVE A TAMPLE WHERE WE CAN CHAGE OUR SELF BECOUSE THE CLASSE SCHEDULE CHANGE OTHER TIME
Nice to have
• THE GRAFIC EXPLAN HOW EFECTIVE THE CLASSES ARE IN EXTREMILY IMPORTANT. WE WANT TO INOVAT AND CRETED SOMETIMNH UNIQUE
• I UP LOAD OUR LOGO, IS SHOULD TO FOLOW OUR COLORS
• ON THE SCHEDUDLE SHOULD HAVE A LOGO

```html
<!DOCTYPE html>
<html lang="en">
<head>
<meta charset="utf-8">
<title>Gym Schedule – Apex Training Center</title>
<link href="https://fonts.googleapis.com/css2?family=Oswald:wght@400;500;600;700&family=Roboto+Condensed:wght@400;700&display=swap" rel="stylesheet">
<style>
  :root{
    --red:#ec1f27;
    --red-dark:#a5141a;
    --black:#000000;
    --ink:#1b1b1b;
    --grey:#9d9d9d;
    --grey-light:#e4e4e4;
    --paper:#f6f6f6;
    --white:#ffffff;
  }
  *{margin:0;padding:0;box-sizing:border-box}
  html,body{width:1200px;height:2239px;overflow:hidden}
  body{background:var(--paper);font-family:"Roboto Condensed",Arial,sans-serif;color:var(--ink);position:relative}

  /* ---------- header ---------- */
  .hero{position:absolute;left:0;top:0;width:1200px;height:610px;
    background:radial-gradient(ellipse at 30% 40%,#2e2e2e 0%,#141414 60%,#0a0a0a 100%)}
  .hero-photo{position:absolute;right:0;top:0;width:500px;height:610px;
    background:linear-gradient(100deg,rgba(20,20,20,0) 0%,#4a3a33 35%,#6b5247 55%,#2a2a2a 100%)}
  .brand{position:absolute;left:97px;top:92px;display:flex;align-items:center;gap:18px}
  .brand-dot{width:70px;height:70px;border-radius:50%;background:var(--grey)}
  .brand-name{font-family:"Oswald",sans-serif;font-weight:600;font-size:40px;line-height:1;color:var(--grey);letter-spacing:1px;text-transform:uppercase}
  .hero-title{position:absolute;left:62px;top:205px;font-family:"Oswald",sans-serif;font-weight:700;font-size:160px;line-height:1;
    color:var(--red);transform:skewX(-12deg);letter-spacing:-2px;text-transform:uppercase;
    background:linear-gradient(180deg,#ff4a50 0%,var(--red) 45%,var(--red-dark) 100%);-webkit-background-clip:text;background-clip:text;-webkit-text-fill-color:transparent}
  .hero-sub{position:absolute;left:67px;top:398px;font-family:"Oswald",sans-serif;font-weight:500;font-size:40px;letter-spacing:4px;color:#d9d9d9;text-transform:uppercase}

  .badge{position:absolute;left:518px;top:473px;width:164px;height:164px;border-radius:50%;background:var(--white);
    border:10px solid var(--grey);display:flex;align-items:center;justify-content:center}
  .badge-name{font-family:"Oswald",sans-serif;font-weight:600;font-size:40px;color:var(--grey);text-transform:uppercase}
  .badge-caption{position:absolute;left:0;width:1200px;top:648px;text-align:center;font-family:"Oswald",sans-serif;font-weight:600;font-size:36px;color:#5a5a5a;text-transform:uppercase}

  /* ---------- framed sections ---------- */
  .frame{position:absolute;left:93px;width:1032px;border:3px solid var(--red)}
  .frame-title{position:absolute;left:50%;top:-40px;transform:translateX(-50%);background:var(--paper);padding:0 34px;
    font-family:"Oswald",sans-serif;font-weight:700;font-size:60px;line-height:80px;color:var(--red);white-space:nowrap;text-transform:uppercase}
  .frame-title::before,.frame-title::after{content:"";position:absolute;top:40px;width:26px;height:3px;background:var(--red)}
  .frame-title::before{left:6px;transform:rotate(-35deg)}
  .frame-title::after{right:6px;transform:rotate(35deg)}

  /* schedule */
  .room{top:727px;height:455px}
  .timetable{position:absolute;left:8px;top:42px;width:1008px;background:var(--white);border:1px solid var(--grey-light)}
  .tt-row{display:grid;grid-template-columns:150px repeat(6,143px);align-items:center;border-bottom:1px solid var(--grey-light)}
  .tt-head{height:44px;background:var(--grey-light)}
  .tt-head span{font-family:"Oswald",sans-serif;font-weight:500;font-size:24px;color:#707070;text-align:center;text-transform:uppercase}
  .tt-row .time{font-family:"Oswald",sans-serif;font-weight:600;font-size:24px;color:var(--red);text-align:center}
  .tt-row .cls{font-size:21px;text-align:center;line-height:1.15;color:#222}
  .r-53{height:53px}.r-52{height:52px}.r-49{height:49px}.r-77{height:77px}.r-60{height:60px}
  .tt-band{height:50px;margin:4px 0;background:var(--black);color:var(--red);font-family:"Oswald",sans-serif;font-weight:600;font-size:28px;
    display:flex;align-items:center;justify-content:center;text-transform:uppercase}

  /* definitions */
  .defs{top:1243px;height:317px}
  .def-grid{position:absolute;left:8px;top:42px;width:1008px;display:grid;grid-template-columns:repeat(5,1fr);gap:3px;background:var(--white)}
  .def-name{height:46px;background:linear-gradient(180deg,#3a3a3a,#0c0c0c);color:#9a9a9a;font-family:"Oswald",sans-serif;font-weight:500;
    font-size:26px;display:flex;align-items:center;justify-content:center;text-transform:uppercase}
  .def-text{height:204px;background:var(--white);border:1px solid var(--grey-light);border-top:none;padding:24px 14px 0;text-align:center;font-size:17px;line-height:1.3;color:#222}

  /* intensity */
  .intensity{top:1619px;height:545px}
  .meter{position:absolute;left:8px;top:45px;width:1008px;height:493px;background:#0d0d0d}
  .m-row{display:grid;grid-template-columns:142px repeat(5,173px);height:90px;border-top:1px solid #2a2a2a}
  .m-head{height:45px;border:none;background:linear-gradient(90deg,#0d0d0d 0 142px,var(--red) 142px)}
  .m-head span{font-family:"Oswald",sans-serif;font-weight:600;font-size:20px;color:var(--white);display:flex;align-items:center;justify-content:center;text-transform:uppercase;border-left:1px solid #b5121a}
  .m-label{font-family:"Oswald",sans-serif;font-weight:500;font-size:18px;line-height:1.2;color:var(--white);padding-left:22px;display:flex;align-items:center;text-transform:uppercase}
  .m-cell{position:relative;background:linear-gradient(180deg,#1f1f1f,#111);border-left:1px solid #2a2a2a}
  .bar{position:absolute;left:19px;top:42px;width:135px;height:14px;
    background:linear-gradient(90deg,#fff26a 0 16.6%,#f9d548 16.6% 33.3%,#f5aa34 33.3% 50%,#f07b2b 50% 66.6%,#e84a25 66.6% 83.3%,#c81c20 83.3%)}
  .mark{position:absolute;top:-12px;width:0;height:0;border-left:7px solid transparent;border-right:7px solid transparent;border-top:9px solid var(--white);transform:translateX(-7px)}
  .scale{position:absolute;left:19px;top:61px;width:135px;display:flex;justify-content:space-between;font-size:9px;color:#bbb}

  .footer{position:absolute;left:0;top:2224px;width:1200px;height:15px;background:var(--black)}
</style>
</head>
<body>

<header class="hero">
  <div class="hero-photo" role="img" aria-label="Athlete in training gear holding dumbbells in a boxing stance"></div>
  <div class="brand"><span class="brand-dot"></span><span class="brand-name">Apex Training Center</span></div>
  <h1 class="hero-title">Gym Schedule</h1>
  <p class="hero-sub">Full schedule and classes roon schedule</p>
</header>

<div class="badge"><span class="badge-name">Apex</span></div>
<div class="badge-caption">Schedule</div>

<section class="frame room">
  <h2 class="frame-title">Fitness Room</h2>
  <div class="timetable">
    <div class="tt-row tt-head"><span></span><span>Monday</span><span>Tuesday</span><span>Wednesday</span><span>Thursday</span><span>Friday</span><span>Saturday</span></div>
    <div class="tt-row r-53"><span class="time">8:30</span><span class="cls">Hiit</span><span class="cls">Crossfit</span><span class="cls">Hiit</span><span class="cls">Crossfit</span><span class="cls">Hiit</span><span class="cls"></span></div>
    <div class="tt-row r-52"><span class="time">9:30</span><span></span><span></span><span></span><span></span><span></span><span></span></div>
    <div class="tt-band">Afternoon Schedule</div>
    <div class="tt-row r-49"><span class="time">4:30</span><span class="cls">Kids Fitness</span><span class="cls">Teen Fitness</span><span class="cls">Kids Fitness</span><span class="cls">Teen Fitness</span><span class="cls">Kids Fitness</span><span></span></div>
    <div class="tt-row r-77"><span class="time">5:30</span><span class="cls">Apex<br>Boot Camp</span><span class="cls">Fitgh<br>Fiteness</span><span class="cls">Apex<br>BootCamp</span><span class="cls">Fitgh<br>Fiteness</span><span class="cls">Apex<br>Boot Camp</span><span></span></div>
    <div class="tt-row r-60" style="border-bottom:none"><span class="time">6:30</span><span class="cls">Cross Fit</span><span class="cls">Hiit</span><span class="cls">Cross Fit</span><span class="cls">Hiit</span><span class="cls">Cross Fit</span><span></span></div>
  </div>
</section>

<section class="frame defs">
  <h2 class="frame-title">Classes Definition</h2>
  <div class="def-grid">
    <div><div class="def-name">Hiit</div><p class="def-text">Kids boxing class teaches basic boxing skills and techniques such as; stance, guard, movement, jab, cross, hook. It increases strength and improves indurance.</p></div>
    <div><div class="def-name">Boot Camp</div><p class="def-text">Kids boxing class teaches basic boxing skills and techniques such as; stance, guard, movement, jab, cross, Hook. It increases strength and improves indurance.</p></div>
    <div><div class="def-name">Cross Fit</div><p class="def-text">Kids boxing class teaches basic boxing skills and techniques such as; stance, guard, movement, jab, cross, hook. It increases strength and improves indurance.</p></div>
    <div><div class="def-name">Tean Fitness</div><p class="def-text">Kids boxing class teaches basic boxing skills and techniques such as; stance, guard, movement, jab, cross, hook. It increases strength and improves indurance.</p></div>
    <div><div class="def-name">Kids Fitness</div><p class="def-text">Kids boxing class teaches basic boxing skills and techniques such as; stance, guard, movement, jab, cross, hook. It increases strength and improves indurance.</p></div>
  </div>
</section>

<section class="frame intensity">
  <h2 class="frame-title">Classes Intensity</h2>
  <div class="meter">
    <div class="m-row m-head"><span style="border:none"></span><span>Hiit</span><span>Boot Camp</span><span>Cross Fit</span><span>Tean Fitness</span><span>Kids Fitness</span></div>

    <div class="m-row"><span class="m-label">Fat Burm -<br>Weigth Lost</span>
      <div class="m-cell"><div class="bar"><i class="mark" style="left:88%"></i></div><div class="scale"><span>Low</span><span>Medium</span><span>High</span></div></div>
      <div class="m-cell"><div class="bar"><i class="mark" style="left:88%"></i></div><div class="scale"><span>Low</span><span>Medium</span><span>High</span></div></div>
      <div class="m-cell"><div class="bar"><i class="mark" style="left:88%"></i></div><div class="scale"><span>Low</span><span>Medium</span><span>High</span></div></div>
      <div class="m-cell"><div class="bar"><i class="mark" style="left:50%"></i></div><div class="scale"><span>Low</span><span>Medium</span><span>High</span></div></div>
      <div class="m-cell"><div class="bar"><i class="mark" style="left:50%"></i></div><div class="scale"><span>Low</span><span>Medium</span><span>High</span></div></div>
    </div>

    <div class="m-row"><span class="m-label">Intensity -<br>Cardio</span>
      <div class="m-cell"><div class="bar"><i class="mark" style="left:88%"></i></div><div class="scale"><span>Low</span><span>Medium</span><span>High</span></div></div>
      <div class="m-cell"><div class="bar"><i class="mark" style="left:50%"></i></div><div class="scale"><span>Low</span><span>Medium</span><span>High</span></div></div>
      <div class="m-cell"><div class="bar"><i class="mark" style="left:88%"></i></div><div class="scale"><span>Low</span><span>Medium</span><span>High</span></div></div>
      <div class="m-cell"><div class="bar"><i class="mark" style="left:50%"></i></div><div class="scale"><span>Low</span><span>Medium</span><span>High</span></div></div>
      <div class="m-cell"><div class="bar"><i class="mark" style="left:50%"></i></div><div class="scale"><span>Low</span><span>Medium</span><span>High</span></div></div>
    </div>

    <div class="m-row"><span class="m-label">Flexibility -<br>Agility</span>
      <div class="m-cell"><div class="bar"><i class="mark" style="left:50%"></i></div><div class="scale"><span>Low</span><span>Medium</span><span>High</span></div></div>
      <div class="m-cell"><div class="bar"><i class="mark" style="left:50%"></i></div><div class="scale"><span>Low</span><span>Medium</span><span>High</span></div></div>
      <div class="m-cell"><div class="bar"><i class="mark" style="left:50%"></i></div><div class="scale"><span>Low</span><span>Medium</span><span>High</span></div></div>
      <div class="m-cell"><div class="bar"><i class="mark" style="left:88%"></i></div><div class="scale"><span>Low</span><span>Medium</span><span>High</span></div></div>
      <div class="m-cell"><div class="bar"><i class="mark" style="left:88%"></i></div><div class="scale"><span>Low</span><span>Medium</span><span>High</span></div></div>
    </div>

    <div class="m-row"><span class="m-label">Power -<br>Strength</span>
      <div class="m-cell"><div class="bar"><i class="mark" style="left:50%"></i></div><div class="scale"><span>Low</span><span>Medium</span><span>High</span></div></div>
      <div class="m-cell"><div class="bar"><i class="mark" style="left:50%"></i></div><div class="scale"><span>Low</span><span>Medium</span><span>High</span></div></div>
      <div class="m-cell"><div class="bar"><i class="mark" style="left:7%"></i></div><div class="scale"><span>Low</span><span>Medium</span><span>High</span></div></div>
      <div class="m-cell"><div class="bar"><i class="mark" style="left:50%"></i></div><div class="scale"><span>Low</span><span>Medium</span><span>High</span></div></div>
      <div class="m-cell"><div class="bar"><i class="mark" style="left:50%"></i></div><div class="scale"><span>Low</span><span>Medium</span><span>High</span></div></div>
    </div>

    <div class="m-row"><span class="m-label">Physical<br>Contact</span>
      <div class="m-cell"><div class="bar"><i class="mark" style="left:7%"></i></div><div class="scale"><span>Low</span><span>Medium</span><span>High</span></div></div>
      <div class="m-cell"><div class="bar"><i class="mark" style="left:7%"></i></div><div class="scale"><span>Low</span><span>Medium</span><span>High</span></div></div>
      <div class="m-cell"><div class="bar"><i class="mark" style="left:7%"></i></div><div class="scale"><span>Low</span><span>Medium</span><span>High</span></div></div>
      <div class="m-cell"><div class="bar"><i class="mark" style="left:7%"></i></div><div class="scale"><span>Low</span><span>Medium</span><span>High</span></div></div>
      <div class="m-cell"><div class="bar"><i class="mark" style="left:7%"></i></div><div class="scale"><span>Low</span><span>Medium</span><span>High</span></div></div>
    </div>
  </div>
</section>

<footer class="footer">
  <svg width="1200" height="15" viewBox="0 0 1200 15" aria-hidden="true">
    <polygon points="1040,15 1052,0 1110,0 1098,15" fill="#ec1f27"/>
    <polygon points="1120,15 1132,0 1190,0 1178,15" fill="#ec1f27"/>
  </svg>
</footer>

</body>
</html>
```